Grand Chart of Bold Reformers

Hi - I would like your help transforming my (terrible) drawing into a graphic that pops -using hex colors I'll give you - so that I can put it into stationary and on t-shirts or tote bags. My company, the Marrowgate Institute, trains social change leaders (from the sectors in the periodic table) on how to lead large-scale change. I have this vision - the "periodic table" but these are the sectors that my clients work in. If you are having trouble reading my writing, I apologize. Our hex colors are: #114769, #76984C, #80B5CF (Seagull), #8F2C63 and Rangoon Black #191919. You don't need to use all of them, but it'd be good to be consistent with our overall branding. If you can't read my writing, I will send correct spelling. The "Marrowgate" with the flowers on the bottom is for a separate design bid.

Target Market(s)

nonprofit, social entrepreneurs, philanthropy, leaders

Requirements
Must have
• clean, readable font. alignment to look like periodic table of elements. heart icon for love, cat face for cats.

```html
<!DOCTYPE html>
<html lang="en">
<head>
<meta charset="utf-8">
<title>Grand Chart of Bold Reformers</title>
<link rel="stylesheet" href="https://fonts.googleapis.com/css2?family=Nunito:wght@800;900&display=swap">
<style>
  :root {
    --frame: #114769;
    --paper: #ffffff;
    --ink: #191919;
    --plum: #8f2c63;
    --seagull: #80b5cf;
    --olive: #76984c;
    --navy: #114769;
    --rule: #191919;
  }
  * { margin: 0; padding: 0; box-sizing: border-box; }
  html, body { width: 1200px; height: 773px; overflow: hidden; }
  body { background: var(--frame); font-family: "Nunito", sans-serif; }
  .poster { position: relative; width: 1200px; height: 773px; background: var(--frame); }
  .sheet { position: absolute; left: 46px; top: 30px; width: 1103px; height: 710px; background: var(--paper); }

  .cell {
    position: absolute;
    left: var(--x); top: var(--y); width: var(--w); height: var(--h);
    border: 5px solid var(--rule);
  }
  .cell.sector-people { background: var(--plum); color: #fff; }
  .cell.sector-rights { background: var(--seagull); color: var(--ink); }
  .cell.sector-life { background: var(--olive); color: #fff; }
  .cell.value { background: var(--navy); color: #fff; }

  .label {
    position: absolute; top: 9px; left: 9px; right: 8px;
    font-weight: 800; font-size: 13px; line-height: 14px;
  }
  .symbol {
    position: absolute; left: 9px; bottom: 4px;
    font-weight: 900; font-size: 54px; line-height: 1; letter-spacing: -1px;
  }
  .cell.value .label { font-size: 15px; line-height: 16px; top: 10px; left: 12px; }
  .cell.value .symbol { left: 12px; bottom: 6px; }

  .cat-figure {
    position: absolute; left: 12px; bottom: 10px; width: 64px; height: 52px;
    border-radius: 20px; background: var(--ink);
  }
  .heart { position: absolute; left: 12px; bottom: 14px; width: 48px; height: 46px; }
</style>
</head>
<body>
<main class="poster">
  <div class="sheet"></div>

  <div class="cell sector-people" style="--x:263px;--y:79px;--w:116px;--h:115px"><span class="label">Anti-<br>violence</span><span class="symbol">Av</span></div>
  <div class="cell sector-people" style="--x:263px;--y:189px;--w:116px;--h:116px"><span class="label">Early<br>Childhood</span><span class="symbol">Ec</span></div>
  <div class="cell sector-people" style="--x:263px;--y:300px;--w:116px;--h:116px"><span class="label">Education</span><span class="symbol">Ed</span></div>
  <div class="cell sector-people" style="--x:263px;--y:411px;--w:116px;--h:115px"><span class="label">Animal<br>Welfare</span><span class="symbol">Aw</span></div>

  <div class="cell sector-rights" style="--x:374px;--y:189px;--w:116px;--h:116px"><span class="label">Climate<br>Change</span><span class="symbol">Cc</span></div>
  <div class="cell sector-rights" style="--x:374px;--y:300px;--w:116px;--h:116px"><span class="label">Arts &amp;<br>Culture</span><span class="symbol">As</span></div>
  <div class="cell sector-rights" style="--x:374px;--y:411px;--w:116px;--h:115px"><span class="label">Cats</span><div class="cat-figure" role="img" aria-label="Cat face icon"></div></div>

  <div class="cell sector-rights" style="--x:485px;--y:189px;--w:117px;--h:116px"><span class="label">Environ-<br>mental Justice</span><span class="symbol">Ej</span></div>
  <div class="cell sector-rights" style="--x:485px;--y:300px;--w:117px;--h:116px"><span class="label">Social<br>Justice</span><span class="symbol">Sj</span></div>
  <div class="cell sector-rights" style="--x:485px;--y:411px;--w:117px;--h:115px"><span class="label">Racial<br>Justice</span><span class="symbol">Rj</span></div>

  <div class="cell sector-rights" style="--x:597px;--y:189px;--w:117px;--h:116px"><span class="label">Human<br>Services</span><span class="symbol">Hs</span></div>
  <div class="cell sector-rights" style="--x:597px;--y:300px;--w:117px;--h:116px"><span class="label">Civil<br>Rights</span><span class="symbol">Cr</span></div>
  <div class="cell sector-rights" style="--x:597px;--y:411px;--w:117px;--h:115px"><span class="label">Immigrant<br>Rights</span><span class="symbol">Av</span></div>

  <div class="cell sector-rights" style="--x:709px;--y:189px;--w:116px;--h:116px"><span class="label">Health<br>Law</span><span class="symbol">Hl</span></div>
  <div class="cell sector-rights" style="--x:709px;--y:300px;--w:116px;--h:116px"><span class="label">Health<br>Equity</span><span class="symbol">He</span></div>
  <div class="cell sector-rights" style="--x:709px;--y:411px;--w:116px;--h:115px"><span class="label">Behavioral<br>Health</span><span class="symbol">Bh</span></div>

  <div class="cell sector-life" style="--x:820px;--y:79px;--w:115px;--h:115px"><span class="label">Belonging</span><span class="symbol">B</span></div>
  <div class="cell sector-life" style="--x:820px;--y:189px;--w:115px;--h:116px"><span class="label">Housing</span><span class="symbol">H</span></div>
  <div class="cell sector-life" style="--x:820px;--y:300px;--w:115px;--h:116px"><span class="label">Jobs</span><span class="symbol">J</span></div>
  <div class="cell sector-life" style="--x:820px;--y:411px;--w:115px;--h:115px"><span class="label">Inter-<br>generational</span><span class="symbol">Ig</span></div>

  <div class="cell value" style="--x:263px;--y:580px;--w:139px;--h:114px"><span class="label">Love</span>
    <svg class="heart" viewBox="0 0 50 48" role="img" aria-label="Heart"><path fill="#fff" d="M25 47 C19 40 2 26 2 14 C2 6 8 1 14 1 C19 1 23 4 25 8 C27 4 31 1 36 1 C42 1 48 6 48 14 C48 26 31 40 25 47 Z"/></svg>
  </div>
  <div class="cell value" style="--x:397px;--y:580px;--w:139px;--h:114px"><span class="label">Authenticity</span><span class="symbol">A</span></div>
  <div class="cell value" style="--x:531px;--y:580px;--w:138px;--h:114px"><span class="label">Humility</span><span class="symbol">H</span></div>
  <div class="cell value" style="--x:664px;--y:580px;--w:139px;--h:114px"><span class="label">Audacity</span><span class="symbol">An</span></div>
  <div class="cell value" style="--x:798px;--y:580px;--w:137px;--h:114px"><span class="label">Justice</span><span class="symbol">J</span></div>
</main>
</body>
</html>
```